Tarn - Stationary Design/Layout

We are a well established clothing design and manufacturing company (Tarn Sourcing) based in London UK, with our own factory in Bangladesh, supplying to many fashion retailers and brands. Our factory has very high environmental and ethical standards with people at its heart. Our quality of garments are second to none.
Our new logo has been proudly developed by the Pixel Guild community last month, we are now in the second phase and need the layout designed for our letterheads, double sided business cards, compliment slip and clothing ticket. Feel as creative as you like, but make sure it looks great!!
***The Logo - the logo design and colour is set and should NOT be changed and stay on a dark grey backround. The logo artwork to use is attached.
***Details to use for the business card:
Dorian Pelham
Direct Line: 020 7946 0158
dorian@tarnsourcing-example.com
Tarn Sourching Ltd.
57 - 59 Hollin Row
Camdon . Swindon
NW9 4QT
Switchboard: 020 7946 0274
Fax: 020 7946 0274
www.tarnsourcing-example.co.uk
***Details to use for the letterhead and compliment slip:
Tarn Sourching Ltd.
57 - 59 Hollin Row
Camdon . Swindon
NW9 4QT
Fax: 020 7946 0274
www.tarnsourcing-example.co.uk
***Details for Swing Ticket:
Size: 12cm height by 5.5cm width
One side need to have just the logo without the 'Sourcing', on the other it needs to stay blank

```html
<!DOCTYPE html>
<html lang="en">
<head>
<meta charset="utf-8">
<title>Tarn Sourcing – Business Card Back</title>
<link rel="stylesheet" href="https://fonts.googleapis.com/css2?family=Didact+Gothic&display=swap">
<style>
  :root {
    --sky-top: #1d7a6c;
    --sky-mid: #3fcfa6;
    --sky-mint: #62ffc9;
    --sky-pale: #dcfff1;
    --grass-light: #8fe02a;
    --grass-mid: #3f8f12;
    --grass-dark: #10260a;
    --ink: #3d3d3d;
  }
  html, body {
    margin: 0;
    padding: 0;
    overflow: hidden;
    background: #ffffff;
  }
  .card {
    position: relative;
    width: 1200px;
    height: 720px;
    overflow: hidden;
    background: linear-gradient(180deg,
      var(--sky-top) 0%,
      var(--sky-mid) 28%,
      var(--sky-mint) 48%,
      #a8ffe0 68%,
      var(--sky-pale) 84%);
    font-family: "Didact Gothic", "Century Gothic", sans-serif;
    color: var(--ink);
  }
  .grass {
    position: absolute;
    left: 0;
    right: 0;
    bottom: 0;
    height: 120px;
    background: linear-gradient(180deg,
      rgba(143, 224, 42, 0) 0%,
      var(--grass-light) 14%,
      var(--grass-mid) 45%,
      var(--grass-dark) 100%);
  }
  .contact {
    position: absolute;
    top: 470px;
    font-size: 31px;
    line-height: 38px;
    letter-spacing: 0.2px;
    white-space: nowrap;
  }
  .contact p { margin: 0; }
  .contact--lines {
    right: 641px;
    text-align: right;
  }
  .contact--address {
    left: 597px;
    text-align: left;
  }
</style>
</head>
<body>
  <main class="card">
    <div class="contact contact--lines">
      <p>Switchboard: 020 7946 0274</p>
      <p>Fax: 020 7946 0274</p>
      <p>www.tarnsourcing-example.co.uk</p>
    </div>
    <div class="contact contact--address">
      <p>Tarn Sourching Ltd.</p>
      <p>57 - 59 Hollin Row,</p>
      <p>Camdon, Swindon, NW9 4QT</p>
    </div>
    <div class="grass" role="img" aria-label="Strip of bright green grass blades along the bottom edge"></div>
  </main>
</body>
</html>
```